New Business Card Design Project

Updated business card design. I am moving towards more coaching of, for the most part women, who are searching for more in their lives. I am an intuitive healer, homeopath and nutritionist but also an author and motivational speaker. Int the past I have included my photo on the card but that is not essential. My book is called the Brilliance of Saffron - Reclaiming the Shade of Your Spirit so my colours are typically magenta.
Target Market(s)
Women - 35 - 60 considering improving their health. However, I am also a professional speaker with a target audience including corporate and conferences.
Industry/Entity Type
Health And Wellness
Contact Information for Business Card
Lucinda Parvell, CNP, RHP, MA
www.lucindaparvell.com
lucinda@lucindaparvell.com
519-362-7015
Facebook, instagram and twitter logos
Look and feel
Each slider illustrates characteristics of the customer's brand and the style your logo design should communicate.

```html
<!DOCTYPE html>
<html lang="en">
<head>
<meta charset="utf-8">
<title>Lucinda Parvell – Business Card</title>
<link rel="stylesheet" href="https://fonts.googleapis.com/css2?family=Cinzel:wght@400;600&family=Questrial&display=swap">
<style>
  :root {
    --magenta: #e9267f;
    --ink-white: #ffffff;
    --soft-white: #fde3ef;
    --page: #efece8;
    --leaf: #5f8a4a;
    --brick: #c9ab86;
    --shirt: #f4f4f2;
    --social: #2f4f86;
  }
  * { box-sizing: border-box; margin: 0; padding: 0; }
  html, body { width: 1200px; height: 1023px; overflow: hidden; }
  body {
    background: var(--page);
    font-family: "Questrial", "Century Gothic", sans-serif;
    color: var(--ink-white);
    position: relative;
  }
  .card {
    position: absolute;
    left: 220px;
    width: 760px;
    height: 434px;
    border-radius: 18px;
    overflow: hidden;
    background: var(--magenta);
    box-shadow: 0 10px 28px rgba(0,0,0,.18);
  }
  .card--front { top: 50px; }
  .card--back  { top: 540px; }

  .photo-panel {
    position: absolute;
    left: 0; top: 0; bottom: 0;
    width: 300px;
    background: linear-gradient(160deg, var(--brick) 0%, #d8c2a2 30%, var(--shirt) 55%, #6e8f5a 80%, var(--leaf) 100%);
  }
  .photo-divider {
    position: absolute;
    left: 300px; top: 0; bottom: 0;
    width: 6px;
    background: var(--ink-white);
  }
  .info {
    position: absolute;
    left: 346px; top: 40px; right: 30px;
  }
  .card--back .info { left: 60px; }

  .brand { display: flex; align-items: center; gap: 12px; }
  .brand-dot {
    width: 22px; height: 22px; border-radius: 50%;
    background: var(--soft-white);
    flex: none;
  }
  .brand-name {
    font-size: 40px;
    letter-spacing: .5px;
    white-space: nowrap;
  }
  .brand-tagline {
    font-size: 13px;
    letter-spacing: 1px;
    margin: 4px 0 0 34px;
    color: var(--soft-white);
  }
  .person-name {
    font-family: "Cinzel", "Trajan Pro", serif;
    font-weight: 600;
    font-size: 30px;
    letter-spacing: 1px;
    margin-top: 34px;
    white-space: nowrap;
  }
  .credentials { font-size: 18px; margin-top: 2px; }
  .address { font-size: 18px; line-height: 1.4; margin-top: 20px; }
  .contact-list { list-style: none; margin-top: 14px; font-size: 18px; line-height: 1.5; }
  .contact-list li { display: flex; align-items: center; gap: 10px; white-space: nowrap; }
  .contact-list svg { width: 14px; height: 14px; flex: none; }

  .social-row {
    position: absolute;
    right: 34px; bottom: 30px;
    display: flex; gap: 10px;
  }
  .social-box {
    width: 24px; height: 24px; border-radius: 3px;
    background: var(--social);
  }
</style>
</head>
<body>

<section class="card card--front">
  <div class="photo-panel" role="img" aria-label="Portrait photograph of the coach seated in front of a brick wall with green leaves"></div>
  <div class="photo-divider"></div>

  <div class="info">
    <div class="brand">
      <span class="brand-dot"></span>
      <span class="brand-name">Lucinda Parvell</span>
    </div>
    <p class="brand-tagline">vitality rebel</p>

    <h1 class="person-name">LUCINDA PARVELL</h1>
    <p class="credentials">CNP, RHP, MA</p>

    <p class="address">418 Elmwood Ave. E., London<br>ON, N5Y 2K4</p>

    <ul class="contact-list">
      <li>
        <svg viewBox="0 0 14 14"><path d="M3 1l2 3-1.3 1.3a7 7 0 0 0 5 5L10 9l3 2-1 2C6 13 1 8 1 2z" fill="#fff"/></svg>
        <span>519-362-7015</span>
      </li>
      <li>
        <svg viewBox="0 0 14 14"><rect x="1" y="3" width="12" height="8" fill="none" stroke="#fff" stroke-width="1.4"/><path d="M1 3l6 5 6-5" fill="none" stroke="#fff" stroke-width="1.4"/></svg>
        <span>lucinda@lucindaparvell.com</span>
      </li>
      <li>
        <svg viewBox="0 0 14 14"><circle cx="7" cy="7" r="5.6" fill="none" stroke="#fff" stroke-width="1.3"/><path d="M1.5 7h11M7 1.5c-3 3-3 8 0 11M7 1.5c3 3 3 8 0 11" fill="none" stroke="#fff" stroke-width="1"/></svg>
        <span>www.lucindaparvell.com</span>
      </li>
    </ul>
  </div>

  <div class="social-row" aria-label="Social media profiles">
    <span class="social-box"></span>
    <span class="social-box"></span>
    <span class="social-box"></span>
  </div>
</section>

<section class="card card--back">
  <div class="info">
    <div class="brand">
      <span class="brand-dot"></span>
      <span class="brand-name">Lucinda Parvell</span>
    </div>
    <p class="brand-tagline">vitality rebel</p>

    <h2 class="person-name">LUCINDA PARVELL</h2>
    <p class="credentials">CNP, RHP, MA</p>
    <p class="address">418 Elmwood Ave. E., London<br>ON, N5Y 2K4</p>
    <ul class="contact-list">
      <li><span>519-362-7015</span></li>
      <li><span>lucinda@lucindaparvell.com</span></li>
      <li><span>www.lucindaparvell.com</span></li>
    </ul>
  </div>
</section>

</body>
</html>
```